Korvanta Business Card

Looking for business card ideas. Company name is Korvanta. Have a few basic ideas on attachment. Please submit anything with the logo and general information from attachment.

Industry/Entity Type

Business

```html
<!DOCTYPE html>
<html lang="en">
<head>
<meta charset="utf-8">
<title>Korvanta Business Card</title>
<link rel="stylesheet" href="https://fonts.googleapis.com/css2?family=Mulish:wght@400;800&display=swap">
<style>
  :root {
    --backdrop: #d9d9d9;
    --card: #ffffff;
    --ink: #111111;
    --brand-red: #d7343a;
    --card-shadow: rgba(0, 0, 0, 0.18);
  }
  html, body {
    margin: 0;
    padding: 0;
    width: 1200px;
    height: 720px;
    overflow: hidden;
    background: var(--backdrop);
    font-family: "Mulish", "Century Gothic", sans-serif;
  }
  .canvas {
    position: relative;
    width: 1200px;
    height: 720px;
    display: flex;
    align-items: center;
    justify-content: center;
  }
  .business-card {
    position: relative;
    width: 1000px;
    height: 572px;
    background: var(--card);
    box-shadow: 0 10px 30px var(--card-shadow);
    color: var(--ink);
  }
  .brand {
    position: absolute;
    left: 44px;
    top: 34px;
    display: flex;
    align-items: center;
    gap: 18px;
  }
  .brand-dot {
    width: 74px;
    height: 74px;
  }
  .brand-name {
    font-size: 46px;
    font-weight: 400;
    color: var(--brand-red);
    letter-spacing: 3px;
  }
  .person-name {
    position: absolute;
    left: 120px;
    top: 150px;
    margin: 0;
    font-size: 32px;
    font-weight: 800;
  }
  .contact-list {
    position: absolute;
    left: 120px;
    top: 214px;
    margin: 0;
    padding: 0;
    list-style: none;
    font-size: 22px;
    line-height: 36px;
  }
  .address {
    position: absolute;
    left: 640px;
    top: 446px;
    margin: 0;
    font-style: normal;
    font-size: 24px;
    line-height: 34px;
  }
</style>
</head>
<body>
<main class="canvas">
  <section class="business-card">
    <div class="brand">
      <svg class="brand-dot" viewBox="0 0 74 74" aria-hidden="true">
        <circle cx="37" cy="37" r="37" fill="var(--brand-red)"/>
      </svg>
      <span class="brand-name">Korvanta</span>
    </div>
    <h1 class="person-name">Dana Morell, Dir.</h1>
    <ul class="contact-list">
      <li>Cell: (555) 014-2290</li>
      <li>Office: (555) 014-3300</li>
      <li>Email: dmorell@brevalo.com</li>
      <li>Website: www.korvanta.org</li>
    </ul>
    <address class="address">
      2048 N. Linden Ave.<br>
      Marlow, TX 79850
    </address>
  </section>
</main>
</body>
</html>
```